Keelbrook Vault Holdings Needs A Website

We are looking for a website for a new company. 4 Pages

Needs to be responsive and mobile friendly for all browsers and coded for both Android & IOS. SEO is also important.

Website Brief – Keelbrook Vault Holdings
Domain: www.keelbrookvault.net
Email: info@keelbrookvault.net
Phone: to be inserted later
Address: 40837 52 Ave, Edmonton, AB T6K 3R8
Platform: WordPress (recommended for flexibility, SEO tools, and ease of editing)
Requirements:
• Responsive & mobile-friendly (Android & iOS)
• Cross-browser compatibility
• Fast page load speed
• SEO optimized for storage development, management, and investment keywords
• Easy in-house editing after launch
• Professional, modern, trust-driven design reflecting expertise, reliability, and innovation
________________________________________
Pages
1. HOME
Purpose: Quickly communicate who Keelbrook Vault Holdings is and why they’re the best choice for designing, building, leasing, and managing self storage facilities.
Content Highlights:
• Hero Section: Large, bold image of a modern self storage facility with headline:
"From Concept to Capacity – Your Self Storage Experts"
• Subheadline: “Keelbrook Vault Holdings delivers turnkey design, construction, leasing, and management services for profitable self storage operations.”
• Quick Service Icons:
o Facility Design & Development
o Construction & Build Management
o Lease-Up & Marketing
o Ongoing Facility Management
• Call to Action Button: “LEARN MORE” → links to ABOUT US page.
• Featured Project Highlights: Showcase a few completed or current projects with photos and stats.
• Contact Banner: “Ready to build your next self storage project? Let’s talk.” → CONTACT page.
2. ABOUT US
Purpose: Build credibility, showcase experience, and explain the value proposition.
Content Highlights:
• Who We Are: Overview of Keelbrook Vault Holdings’ history, mission, and team expertise.
• Our Approach: End-to-end process from site selection to occupancy.
• Why Choose Us:
o Industry expertise in self storage
o Proven track record in lease-up success
o Strong vendor and contractor network
3. SERVICES
Purpose: Detail all service offerings with clarity and authority.
Sections:
• Design & Development: Market analysis, site planning, and architectural design.
• Construction Management: Overseeing timelines, budgets, and quality control.
• Lease-Up Strategy: Marketing, promotions, and occupancy acceleration.
• Ongoing Facility Management: Staffing, maintenance, revenue optimization.

4. CONTACT
Purpose: Provide simple, direct ways to connect.
Content Highlights:
• Contact Form (Name, Email, Phone, Message)
• Direct Email: info@keelbrookvault.net
• Phone (if applicable)
• Google Map embed (if there’s a head office location)
• CTA: “Let’s Build Your Storage Success Story.”
Design & Technical Notes
• Visual Style: Clean, modern, bold typography, professional color palette (to be based on branding), strong imagery of self storage facilities.
• Performance: Image compression, caching, responsive scaling.
• SEO Targets: “Self storage facility developer,” “self storage construction,” “self storage management company,” “lease-up services for self storage.”

WordPress or Joomla – must be desktop and mobile friendly with fast page load speed. Need the ability to edit ourselves.

Use pantone colours - #033c5a – dark blue
#2baadf – light blue

```html
<!DOCTYPE html>
<html lang="en">
<head>
<meta charset="utf-8">
<title>Keelbrook Vault Holdings – Self Storage Experts</title>
<link href="https://fonts.googleapis.com/css2?family=Poppins:wght@400;500;600&display=swap" rel="stylesheet">
<style>
:root{
  --dark:#033c5a;
  --light:#2baadf;
  --pale:#e3f3fb;
  --ink:#111;
  --white:#fff;
  --card-line:#e4e4e4;
}
*{margin:0;padding:0;box-sizing:border-box}
html,body{width:1200px;height:3950px;overflow:hidden}
body{position:relative;background:var(--white);font-family:'Poppins',sans-serif;color:var(--ink)}
.abs{position:absolute}

/* hero */
.hero{left:0;top:0;width:1200px;height:958px;
  background:linear-gradient(180deg,#28506f 0%,#2c6f9e 30%,#2a96cc 52%,var(--light) 64%,var(--light) 100%)}
.hero-shape{left:0;top:0;width:1200px;height:958px}
.site-header{left:35px;top:35px;width:1127px;height:103px;background:var(--white);border-radius:52px}
.brand{left:70px;top:69px;display:flex;align-items:center;gap:10px}
.brand-square{width:28px;height:28px;background:var(--dark);border-radius:4px}
.brand-name{font-weight:600;font-size:21px;color:var(--dark);white-space:nowrap}
.main-nav{left:564px;top:75px;font-size:14px}
.main-nav a{text-decoration:none;color:#222;position:absolute;white-space:nowrap}
.main-nav a.active{color:var(--light);font-weight:500}
.btn-header{left:963px;top:61px;width:172px;height:49px;border-radius:25px;background:var(--light);color:var(--white);
  font-size:14px;font-weight:500;display:flex;align-items:center;justify-content:center}
.hero-title{left:0;top:552px;width:1200px;text-align:center;color:var(--white);font-weight:600;font-size:50px;line-height:60px}
.hero-sub{left:0;top:691px;width:1200px;text-align:center;color:var(--white);font-size:16.5px;line-height:27px}
.btn-hero{left:494px;top:774px;width:236px;height:58px;border-radius:29px;background:var(--white);color:var(--light);
  font-size:15px;font-weight:500;display:flex;align-items:center;justify-content:center}

/* section titles */
.section-title{left:0;width:1200px;text-align:center;font-weight:600;font-size:41px;color:var(--dark)}
.section-title span{color:var(--light)}
.rule{height:3px;background:var(--dark)}

/* services */
.service-card{top:1197px;width:236px;height:255px;background:var(--white);box-shadow:0 2px 10px rgba(0,0,0,.14);
  border-bottom:6px solid var(--dark);border-radius:3px}
.service-icon{position:absolute;left:63px;top:30px;width:110px;height:100px}
.service-name{position:absolute;left:0;top:158px;width:236px;text-align:center;font-weight:500;font-size:22px;line-height:28px;color:var(--ink)}

/* about */
.about-title{left:72px;top:1560px;font-weight:600;font-size:41px;color:var(--dark)}
.about-title span{color:var(--light)}
.about-lead{left:70px;top:1664px;width:500px;font-size:20px;line-height:33px;color:var(--ink)}
.about-text{left:70px;top:1742px;width:500px;font-size:13.6px;line-height:26.7px;color:var(--ink);text-align:justify}
.btn-dark{left:67px;top:2036px;width:177px;height:52px;background:var(--dark);border-radius:4px;color:var(--white);
  font-size:16px;font-weight:500;display:flex;align-items:center;justify-content:center}
.about-visual{left:615px;top:1594px;width:492px;height:503px;
  background:linear-gradient(180deg,#4b5557 0%,#7c7366 45%,#b9ab98 75%,#e6e3de 100%)}

/* projects */
.project-card{top:2341px;width:486px;height:417px;border:2px solid var(--card-line);border-radius:6px;background:var(--white)}
.project-photo{position:absolute;left:15px;top:15px;width:453px;height:320px;border-radius:6px}
.project-caption{position:absolute;left:0;top:364px;width:482px;text-align:center;font-size:21px;font-weight:500;color:var(--ink)}

/* cta */
.cta{left:0;top:2870px;width:1200px;height:750px;
  background:linear-gradient(100deg,#2d4e63 0%,#1f4560 40%,#27506a 70%,#3a5f74 100%)}
.cta-title{left:0;top:3054px;width:1200px;text-align:center;color:var(--white);font-weight:600;font-size:51px;line-height:64px}
.btn-cta{left:512px;top:3226px;width:175px;height:55px;background:var(--white);border-radius:4px;color:var(--dark);
  font-weight:600;font-size:16px;display:flex;align-items:center;justify-content:center}
.cta-shape{left:0;top:3420px;width:1200px;height:200px}

/* footer */
.footer-brand{left:164px;top:3660px;display:flex;align-items:center;gap:10px}
.social{top:3716px;width:29px;height:29px;border-radius:50%;background:var(--light)}
.footer-heading{top:3570px;font-size:26px;font-weight:500;color:var(--dark)}
.footer-heading-rule{height:2px;background:#d7d7d7}
.footer-links{left:526px;top:3642px;list-style:none;font-size:15px;color:#222}
.footer-links li{height:32.5px;display:flex;align-items:center;gap:14px}
.footer-links li::before{content:"";width:10px;height:10px;border-radius:50%;background:var(--light)}
.contact-icon{left:800px;width:36px;height:36px;border-radius:50%;background:var(--light);display:flex;align-items:center;justify-content:center}
.contact-text{left:849px;font-size:15.5px;line-height:26px;color:#222}
.footer-line{left:74px;top:3860px;width:1063px;height:1px;background:#bdbdbd}
.copyright{left:0;top:3891px;width:1200px;text-align:center;font-size:15px;color:#222}
</style>
</head>
<body>

<!-- Hero -->
<div class="abs hero" role="img" aria-label="Modern warehouse loading bay with a truck at the dock, fading into brand blue"></div>
<svg class="abs hero-shape" viewBox="0 0 1200 958" aria-hidden="true">
  <polygon points="0,808 603,928 1200,808 1200,836 603,958 0,836" fill="#033c5a"/>
  <polygon points="0,836 603,958 1200,836 1200,958 0,958" fill="#fff"/>
</svg>

<header class="abs site-header"></header>
<div class="abs brand"><div class="brand-square"></div><div class="brand-name">Keelbrook Vault Holdings</div></div>
<nav class="abs main-nav">
  <a class="active" style="left:0">Home</a>
  <a style="left:69px">About Us</a>
  <a style="left:158px">Services</a>
  <a style="left:244px">Featured Project</a>
</nav>
<div class="abs btn-header">CONTACT US</div>

<h1 class="abs hero-title">From Concept to Capacity – Your<br>Self Storage Experts</h1>
<p class="abs hero-sub">Keelbrook Vault Holdings delivers turnkey design, construction, leasing, and<br>management services for profitable self storage operations.</p>
<div class="abs btn-hero">CONTACT NOW</div>

<!-- Services -->
<h2 class="abs section-title" style="top:1068px">Our <span>Services</span></h2>
<div class="abs rule" style="left:556px;top:1134px;width:88px"></div>

<div class="abs service-card" style="left:81px">
  <svg class="service-icon" viewBox="0 0 110 100" role="img" aria-label="Building with gear icon">
    <ellipse cx="60" cy="55" rx="42" ry="36" fill="#e3f3fb"/>
    <g fill="none" stroke="#2baadf" stroke-width="3">
      <rect x="12" y="30" width="48" height="62"/>
      <path d="M20 40h8M36 40h8M20 52h8M36 52h8M20 64h8M36 64h8M30 92V78h12v14"/>
      <circle cx="78" cy="30" r="14" stroke-width="6" stroke-dasharray="4.4 4.4"/>
      <circle cx="78" cy="30" r="8"/>
    </g>
  </svg>
  <div class="service-name">Facility Design &amp;<br>Development</div>
</div>
<div class="abs service-card" style="left:350px">
  <svg class="service-icon" viewBox="0 0 110 100" role="img" aria-label="Construction crane icon">
    <ellipse cx="55" cy="55" rx="44" ry="36" fill="#e3f3fb"/>
    <g fill="none" stroke="#2baadf" stroke-width="3">
      <path d="M30 92V18M22 92h20M14 24h70M30 18l-14 6M70 24v18"/>
      <rect x="64" y="42" width="12" height="8"/>
      <rect x="52" y="58" width="38" height="34"/>
      <path d="M60 66h8M74 66h8M60 78h8M74 78h8"/>
    </g>
  </svg>
  <div class="service-name">Construction &amp;<br>Build Management</div>
</div>
<div class="abs service-card" style="left:619px">
  <svg class="service-icon" viewBox="0 0 110 100" role="img" aria-label="Upward arrow with percent icon">
    <ellipse cx="55" cy="55" rx="44" ry="36" fill="#e3f3fb"/>
    <g fill="none" stroke="#2baadf" stroke-width="3">
      <path d="M55 8L32 34h13v32h20V34h13z"/>
      <path d="M48 56l14-16"/>
      <circle cx="50" cy="42" r="3"/><circle cx="60" cy="54" r="3"/>
      <path d="M50 74v6M60 74v6M50 88v4M60 88v4" stroke-dasharray="3 3"/>
    </g>
  </svg>
  <div class="service-name">Lease-Up &amp;<br>Marketing</div>
</div>
<div class="abs service-card" style="left:888px">
  <svg class="service-icon" viewBox="0 0 110 100" role="img" aria-label="Gear with rising arrows icon">
    <ellipse cx="55" cy="55" rx="44" ry="36" fill="#e3f3fb"/>
    <g fill="none" stroke="#2baadf" stroke-width="3">
      <circle cx="42" cy="60" r="18" stroke-width="7" stroke-dasharray="5 4.4"/>
      <circle cx="42" cy="60" r="10"/>
      <circle cx="42" cy="60" r="4"/>
      <path d="M60 40V14M52 22l8-8 8 8M74 40V24M68 30l6-6 6 6"/>
      <circle cx="76" cy="72" r="12"/>
      <path d="M76 64v8h6"/>
    </g>
  </svg>
  <div class="service-name">Ongoing Facility<br>Management</div>
</div>

<!-- About -->
<h2 class="abs about-title">About <span>Us</span></h2>
<div class="abs rule" style="left:72px;top:1625px;width:90px"></div>
<p class="abs about-lead">Lorem ipsum dolor sit amet, consectetur<br>adipiscing elit,</p>
<p class="abs about-text">sed do eiusmod tempor incididunt ut labore et dolore magna aliqua. Ut enim ad minim veniam, quis nostrud exercitation ullamco laboris nisi ut aliquip ex ea commodo consequat. Duis aute irure dolor in reprehenderit in voluptate velit esse cillum dolore eu fugiat nulla pariatur. Excepteur sint occaecat cupidatat non proident, sunt in culpa qui officia deserunt mollit anim id est laborum. sed do eiusmod tempor incididunt ut labore et dolore magna aliqua. Ut enim ad minim veniam, quis nostrud exercitation ullamco laboris nisi ut aliquip ex ea commodo consequat. Duis aute irure dolor in reprehenderit in voluptate velit esse cillum dolore eu fugiat nulla pariatur..</p>
<div class="abs btn-dark">Learn More</div>

<div class="abs about-visual" role="img" aria-label="Warehouse aisle lined with stocked shelving"></div>

<!-- Featured projects -->
<h2 class="abs section-title" style="top:2210px">Featured <span>Project</span></h2>
<div class="abs rule" style="left:556px;top:2277px;width:88px"></div>

<div class="abs project-card" style="left:97px">
  <div class="project-photo" role="img" aria-label="Two closed grey-blue roll-up storage doors" style="background:linear-gradient(180deg,#7f9ea1 0%,#6d8f98 60%,#8d8a7a 100%)"></div>
  <div class="project-caption">Lorem ipsum dolor sit amet</div>
</div>
<div class="abs project-card" style="left:601px">
  <div class="project-photo" role="img" aria-label="Warehouse aisle lined with orange pallet racking" style="background:linear-gradient(90deg,#6b4a3c 0%,#c0623e 35%,#a7a39a 55%,#c86a42 75%,#5c4840 100%)"></div>
  <div class="project-caption">Lorem ipsum dolor sit amet</div>
</div>

<!-- Call to action -->
<div class="abs cta" role="img" aria-label="Corridor of self storage units with closed roll-up doors under a dark blue tint"></div>
<h2 class="abs cta-title">Ready to Build Your Next<br>Self Storage Project? Let’s Talk.</h2>
<div class="abs btn-cta">Contact Us</div>
<svg class="abs cta-shape" viewBox="0 0 1200 200" aria-hidden="true">
  <polygon points="0,128 600,25 1200,128 1200,200 0,200" fill="#2baadf"/>
  <polygon points="0,158 600,55 1200,158 1200,200 0,200" fill="#fff"/>
</svg>

<!-- Footer -->
<div class="abs footer-brand"><div class="brand-square"></div><div class="brand-name">Keelbrook Vault Holdings</div></div>
<div class="abs social" style="left:224px"></div>
<div class="abs social" style="left:260px"></div>
<div class="abs social" style="left:297px"></div>

<h3 class="abs footer-heading" style="left:526px">Links</h3>
<div class="abs footer-heading-rule" style="left:516px;top:3612px;width:90px"></div>
<ul class="abs footer-links">
  <li>About us</li>
  <li>Services</li>
  <li>Featured Project</li>
  <li>Contact Us</li>
</ul>

<h3 class="abs footer-heading" style="left:800px">Contact Us</h3>
<div class="abs footer-heading-rule" style="left:788px;top:3625px;width:160px"></div>

<div class="abs contact-icon" style="top:3648px">
  <svg width="16" height="20" viewBox="0 0 16 20"><path d="M8 0C3.6 0 0 3.5 0 7.8 0 13.5 8 20 8 20s8-6.5 8-12.2C16 3.5 12.4 0 8 0zm0 11a3.2 3.2 0 1 1 0-6.4A3.2 3.2 0 0 1 8 11z" fill="#fff"/></svg>
</div>
<p class="abs contact-text" style="top:3652px">Lorem ipsum,Lorem ipsum,<br>Lorem ipsum</p>

<div class="abs contact-icon" style="top:3715px">
  <svg width="18" height="18" viewBox="0 0 24 24"><path d="M6.6 10.8a15.1 15.1 0 0 0 6.6 6.6l2.2-2.2c.3-.3.7-.4 1-.2 1.1.4 2.3.6 3.6.6.6 0 1 .4 1 1V20c0 .6-.4 1-1 1A17 17 0 0 1 3 4c0-.6.4-1 1-1h3.5c.6 0 1 .4 1 1 0 1.3.2 2.5.6 3.6.1.3 0 .7-.2 1z" fill="#fff"/></svg>
</div>
<p class="abs contact-text" style="top:3720px">780 555 0142</p>

<div class="abs contact-icon" style="top:3765px">
  <svg width="18" height="14" viewBox="0 0 18 14"><rect x="0.5" y="0.5" width="17" height="13" rx="1.5" fill="#fff"/><path d="M1 1.5l8 6 8-6" stroke="#2baadf" stroke-width="1.6" fill="none"/></svg>
</div>
<p class="abs contact-text" style="top:3770px">info@keelbrookvault.net</p>

<div class="abs footer-line"></div>
<p class="abs copyright">Copyright © 2025 All Rights Reserved By Keelbrook Vault Holdings</p>

</body>
</html>
```